Banner for construction site to identify developer

we need a 4 foot by 8 foot banner to hang on the fence of a residential townhome development in Phoenix, Arizona that identifies Tollen Ridge as the company behind the development/project. Also needs to include the logo, phone number, and web address. Would like to stick with the blue colors provided in the attached logo. The blues should stay the same but the letters in the logo can change to another color if necessary. Feel free to use "Tollen Ridge" in place of "Tollen Ridge Group". Looking for use of colors/design to take up space so banner is not just text with a logo.

Target Market(s)

drive by traffic looking at the site

Industry/Entity Type

Real Estate

Colors
0054AA
0677BA
7BADD7
CADEEF
E8F1F8

Requirements
Must have
• company name, phone number and web address

```html
<!DOCTYPE html>
<html lang="en">
<head>
<meta charset="utf-8">
<title>Tollen Ridge – Site Banner</title>
<link href="https://fonts.googleapis.com/css2?family=Fira+Sans:wght@500;600&family=Fira+Sans+Condensed:wght@500&display=swap" rel="stylesheet">
<style>
  :root {
    --blue-deep: #0054AA;
    --blue-mid: #0677BA;
    --blue-soft: #7BADD7;
    --blue-pale: #CADEEF;
    --blue-mist: #E8F1F8;
    --ink: #1d3f96;
    --white: #ffffff;
    --backdrop: #e4e5e6;
  }
  html, body {
    margin: 0;
    width: 1200px;
    height: 881px;
    overflow: hidden;
    background: var(--backdrop);
  }
  .banner {
    position: absolute;
    left: 0;
    top: 140px;
    width: 1200px;
    height: 600px;
    overflow: hidden;
    background: linear-gradient(180deg, var(--blue-mist) 0%, var(--blue-pale) 100%);
    font-family: "Fira Sans", sans-serif;
  }
  .banner-band {
    position: absolute;
    inset: 0;
  }
  .brand {
    position: absolute;
    left: 60px;
    top: 220px;
    display: flex;
    align-items: center;
    gap: 34px;
  }
  .brand-mark {
    width: 96px;
    height: 96px;
    background: var(--white);
  }
  .brand-name {
    margin: 0;
    color: var(--white);
    font-weight: 600;
    font-size: 128px;
    line-height: 1;
    letter-spacing: -1px;
  }
  .contact {
    position: absolute;
    left: 60px;
    top: 458px;
    color: var(--ink);
    font-weight: 500;
    font-size: 44px;
    line-height: 58px;
  }
  .address {
    position: absolute;
    right: 60px;
    top: 492px;
    text-align: right;
    color: var(--ink);
    font-family: "Fira Sans Condensed", sans-serif;
    font-weight: 500;
    font-size: 27px;
    line-height: 38px;
  }
  .contact p, .address p { margin: 0; }
</style>
</head>
<body>
  <section class="banner" aria-label="Tollen Ridge construction site banner">
    <svg class="banner-band" viewBox="0 0 1200 600" width="1200" height="600" aria-hidden="false">
      <defs>
        <linearGradient id="bandFill" x1="0" y1="0" x2="1" y2="1">
          <stop offset="0" stop-color="#0677BA"/>
          <stop offset="0.45" stop-color="#0054AA"/>
          <stop offset="1" stop-color="#0054AA"/>
        </linearGradient>
      </defs>
      <polygon points="0,0 400,0 1200,130 1200,456 0,372" fill="url(#bandFill)"/>
      <rect x="620" y="120" width="560" height="300" fill="#0677BA" opacity="0.12" role="img" aria-label="Faint line drawing of townhome buildings"/>
    </svg>

    <div class="brand">
      <span class="brand-mark" aria-hidden="true"></span>
      <h1 class="brand-name">Tollen Ridge</h1>
    </div>

    <div class="contact">
      <p class="contact-phone">(480) 555-0147</p>
      <p class="contact-web">tollenridgegroup.com</p>
    </div>

    <div class="address">
      <p>4120 N. Mesa Vista Dr Suite 210</p>
      <p>Phoenix, AZ 85016</p>
    </div>
  </section>
</body>
</html>
```